Electrical Contracting business card design

We need a simple business card design for an Electrical Contracting business. A simple design would be appreciated
This company has 2 directors so on one it would have Colin Marsh & another with Dana Marsh.
Updates

Reason: Hello A few designers have asked for a logo unfortunately we don't have one so have extended deadline to see who can help us out with this. CHEERS

Reason: Waiting for business partner to return from xmas break. cheers

Industry/Entity Type

Business

Contact Information for Business Card

Volmera Electrical Services P/L
REC: 36074
Residential Commercial Industrial
Service-Repairs-Renovations-Installations-Telephone-Data
Colin Marsh-Ph: 0433 517 862
Email: colin@volmeraelectrical.com.au

Requirements
Should not have
• The design should not have any electrical appliances in it ie: power-points, leads, houses etc.

```html
<!DOCTYPE html>
<html lang="en">
<head>
<meta charset="utf-8">
<title>Volmera Electrical Services – Business Cards</title>
<link rel="stylesheet" href="https://fonts.googleapis.com/css2?family=Josefin+Sans:wght@300;400&family=Oswald:wght@600&display=swap">
<style>
  :root {
    --page: #e9e7e4;
    --card-black: #0d0d0d;
    --accent: #f7901e;
    --ink-dark: #121212;
  }
  * { margin: 0; padding: 0; box-sizing: border-box; }
  html, body { width: 1200px; height: 728px; overflow: hidden; }
  body {
    background: var(--page);
    position: relative;
    font-family: "Josefin Sans", sans-serif;
  }
  .card {
    position: absolute;
    top: 199px;
    width: 540px;
    height: 330px;
    background: var(--card-black);
    overflow: hidden;
    box-shadow: 0 6px 18px rgba(0,0,0,0.18);
  }
  .card--front { left: 40px; display: flex; align-items: center; justify-content: center; }
  .card--back { left: 620px; }

  .wordmark {
    font-family: "Oswald", sans-serif;
    font-weight: 600;
    color: var(--accent);
    font-size: 22px;
    letter-spacing: 0.5px;
    text-transform: uppercase;
  }

  .contact {
    position: absolute;
    color: var(--accent);
    font-weight: 300;
    font-size: 10px;
    line-height: 12px;
    letter-spacing: 0.2px;
  }
  .contact--left { top: 30px; right: 290px; text-align: right; }
  .contact--right { top: 74px; left: 290px; text-align: left; }
  .contact__name { font-size: 18px; line-height: 22px; font-weight: 400; }
  .contact__role { margin-bottom: 1px; }

  .divider {
    position: absolute;
    left: 269px;
    top: 46px;
    width: 2px;
    height: 150px;
    background: var(--accent);
  }

  .band {
    position: absolute;
    left: 0; right: 0; bottom: 0;
    height: 92px;
    background: var(--accent);
    display: flex;
    align-items: flex-end;
    justify-content: flex-end;
    padding: 0 30px 20px 0;
  }
  .band .wordmark { color: var(--ink-dark); font-size: 16px; }
</style>
</head>
<body>
  <section class="card card--front">
    <h1 class="wordmark">Volmera Electrical</h1>
  </section>

  <section class="card card--back">
    <div class="contact contact--left">
      <p class="contact__name">Colin Marsh</p>
      <p class="contact__role">Directors</p>
      <p>0433 517 862</p>
      <p>Email: colin@volmeraelectrical.com.au</p>
      <p>P/L REC: 36074</p>
      <p>Residential Commercial</p>
      <p>IndustrialService</p>
      <p>Repairs</p>
      <p>Renovations</p>
      <p>Installations</p>
      <p>Telephone</p>
      <p>Data</p>
    </div>

    <div class="divider"></div>

    <div class="contact contact--right">
      <p class="contact__name">Dana Marsh</p>
      <p class="contact__role">Directors</p>
      <p>0433 517 862</p>
      <p>Email: colin@volmeraelectrical.com.au</p>
      <p>P/L REC: 36074</p>
      <p>Residential Commercial</p>
      <p>IndustrialService</p>
      <p>Repairs</p>
      <p>Renovations</p>
      <p>Installations</p>
      <p>Telephone</p>
      <p>Data</p>
    </div>

    <div class="band">
      <p class="wordmark">Volmera Electrical Services</p>
    </div>
  </section>
</body>
</html>
```